business card for horse saddlery

after a new business card for our saddlery, i will add 2 logos we have previously used and they can be used (or not) . Any images can be used from our website also at www.bramwoods.net.au, I have also added our brand logo, which may be good to incorporate on back ? we have over 15, 000 items online, ship Australia Wide.

Target Market(s)

horse owners

Industry/Entity Type

Retail - Equestrian

Contact Information for Business Card

Bramwood Horse Supplies, 1300 62 48 07, www.bramwoods.net.au, 278 Tallowmere Rd Corrindale Q 4602

Requirements
Must have
• ridelark is our brand so ridelark logo on back as 'distributers of', easy to read
Nice to have
• professional but fun
Should not have
• double sided (description wont save double sided)

```html
<!DOCTYPE html>
<html lang="en">
<head>
<meta charset="utf-8">
<title>Bramwood Horse Supplies – Business Card</title>
<link rel="stylesheet" href="https://fonts.googleapis.com/css2?family=Lobster&family=Poppins:wght@400;500&display=swap">
<style>
  :root {
    --navy: #243a75;
    --gold: #fbb41c;
    --white: #ffffff;
    --backdrop: #dedede;
    --rule: #e2e2e2;
  }
  * { margin: 0; padding: 0; box-sizing: border-box; }
  html, body { width: 1029px; height: 1200px; overflow: hidden; }
  body {
    background: var(--backdrop);
    font-family: "Poppins", sans-serif;
    position: relative;
  }
  .card {
    position: absolute;
    left: 176px;
    width: 677px;
    height: 386px;
    border-radius: 22px;
    overflow: hidden;
    background: var(--white);
    box-shadow: 0 4px 10px rgba(0,0,0,0.25);
  }
  .card--front { top: 162px; }
  .card--back { top: 680px; }

  .panel { position: absolute; top: 0; height: 100%; }
  .panel--navy { background: var(--navy); }
  .card--front .panel--navy { left: 0; width: 340px; }
  .card--back .panel--navy { left: 339px; right: 0; }

  .accent-bar { position: absolute; top: 0; width: 5px; background: var(--gold); }
  .card--front .accent-bar { left: 340px; height: 112px; }
  .card--back .accent-bar { left: 334px; height: 96px; }

  .brand-mark {
    position: absolute;
    left: 0;
    width: 339px;
    top: 134px;
    display: flex;
    flex-direction: column;
    align-items: center;
    gap: 10px;
    font-weight: 500;
    font-size: 22px;
    line-height: 28px;
    text-align: center;
  }
  .brand-mark__dot { width: 40px; height: 40px; border-radius: 50%; flex: none; }
  .brand-mark__name { display: block; max-width: 200px; }
  .card--front .brand-mark { color: var(--white); }
  .card--front .brand-mark__dot { background: var(--white); }
  .card--back .brand-mark { color: var(--navy); }
  .card--back .brand-mark__dot { background: var(--gold); }

  .back-fold { position: absolute; left: 0; top: 166px; width: 339px; height: 1px; background: var(--rule); }

  .partners {
    position: absolute;
    left: 345px; right: 0; top: 158px; height: 71px;
    display: flex; align-items: center; justify-content: center;
  }
  .partner { color: var(--navy); font-weight: 500; font-size: 19px; width: 140px; text-align: center; }
  .partner--brand { letter-spacing: 1px; text-transform: uppercase; }
  .partners__divider { width: 1px; height: 71px; background: var(--navy); opacity: 0.6; margin: 0 6px; }

  .contact { position: absolute; left: 359px; top: 0; color: var(--white); }
  .contact__name {
    font-family: "Lobster", cursive;
    font-weight: 400;
    font-size: 23px;
    position: absolute; top: 99px; left: 0;
    white-space: nowrap;
  }
  .contact__underline { position: absolute; top: 141px; left: 0; width: 83px; height: 3px; background: var(--gold); }
  .contact__list { list-style: none; position: absolute; left: 0; top: 187px; }
  .contact__item {
    display: flex; align-items: center; gap: 8px;
    font-size: 15.5px; height: 24px; margin-bottom: 12px;
    white-space: nowrap;
  }
  .contact__item--address { font-size: 13.5px; }
  .contact__icon { width: 20px; height: 20px; flex: none; }
</style>
</head>
<body>

<section class="card card--front" aria-label="Card front">
  <div class="panel panel--navy"></div>
  <div class="brand-mark"><span class="brand-mark__dot"></span><span class="brand-mark__name">Bramwood Horse Supplies</span></div>
  <div class="accent-bar"></div>
  <div class="partners">
    <span class="partner">bramwoods</span>
    <span class="partners__divider"></span>
    <span class="partner partner--brand">ridelark</span>
  </div>
</section>

<section class="card card--back" aria-label="Card back">
  <div class="back-fold"></div>
  <div class="brand-mark"><span class="brand-mark__dot"></span><span class="brand-mark__name">Bramwood Horse Supplies</span></div>
  <div class="panel panel--navy"></div>
  <div class="accent-bar"></div>
  <div class="contact">
    <h1 class="contact__name">Bramwood Horse Supplies</h1>
    <div class="contact__underline"></div>
    <ul class="contact__list">
      <li class="contact__item">
        <svg class="contact__icon" viewBox="0 0 20 20" aria-hidden="true">
          <rect x="1" y="1" width="18" height="18" fill="none" stroke="#fbb41c" stroke-width="1.6"/>
          <path d="M6.5 5.5l2 0 .8 2.2-1.2 1c.6 1.2 1.4 2 2.6 2.6l1-1.2 2.2.8v2c-4 .3-7.6-3.3-7.4-7.4z" fill="#fbb41c"/>
        </svg>
        1300 62 48 07
      </li>
      <li class="contact__item">
        <svg class="contact__icon" viewBox="0 0 20 20" aria-hidden="true">
          <rect x="1" y="1" width="18" height="18" fill="none" stroke="#fbb41c" stroke-width="1.6"/>
          <path d="M8 5.5v8.5l2-2 1.6 3.2 1.2-.6-1.6-3.1h2.8z" fill="#fbb41c"/>
        </svg>
        www.bramwoods.net.au
      </li>
      <li class="contact__item contact__item--address">
        <svg class="contact__icon" viewBox="0 0 20 20" aria-hidden="true">
          <rect x="1" y="1" width="18" height="18" fill="none" stroke="#fbb41c" stroke-width="1.6"/>
          <path d="M10 4.5a3.6 3.6 0 0 0-3.6 3.6c0 2.7 3.6 7 3.6 7s3.6-4.3 3.6-7A3.6 3.6 0 0 0 10 4.5zm0 5a1.4 1.4 0 1 1 0-2.8 1.4 1.4 0 0 1 0 2.8z" fill="#fbb41c"/>
        </svg>
        278, Tallowmere Rd, Corrindale Q 4602
      </li>
    </ul>
  </div>
</section>

</body>
</html>
```